Maple Glow Label

Design a label for new brand called Maple Glow. The specific product label :
Maple Glow Cocoa Butter Lotion. You only need to design the front label.
I have included the logo and a bottle jpeg with 2 bottles on it. Please try your best.

Requirements
Must have
• text on the label other than the logo:
cocoa butter
lotion
8.5oz/250ml

Original Moisturizing Formula
Smoothes Marks
Protect Skin

__________________________________
- ALTERNATIVE TEXT TO ALSO USE:
Smoothes Dry Skin, Blemishes & Stretch Marks
Softens Hands, Face and Body
Vitamin E

```html
<!DOCTYPE html>
<html lang="en">
<head>
<meta charset="utf-8">
<title>Maple Glow Cocoa Butter Lotion – Front Label</title>
<link rel="stylesheet" href="https://fonts.googleapis.com/css2?family=Arimo:wght@400;700&display=swap">
<style>
  :root {
    --page-bg: #ece0bf;
    --label-cream: #f8f5e4;
    --lime: #a4cf23;
    --lime-light: #b9dc45;
    --swoosh-cream: #f1ecd3;
    --swoosh-edge: #f6f2b8;
    --brand-green: #1f7b3c;
    --ink: #2a2a22;
    --cocoa-dark: #6a3a1c;
    --cocoa-mid: #a8642e;
    --leaf: #8fbf55;
  }
  * { margin: 0; padding: 0; box-sizing: border-box; }
  html, body {
    width: 959px; height: 1200px; overflow: hidden;
    background: var(--page-bg);
    font-family: "Arimo", Arial, sans-serif;
  }
  .label {
    position: absolute;
    left: 184px; top: 85px;
    width: 590px; height: 1030px;
    background: var(--label-cream);
    border-radius: 46px;
    overflow: hidden;
    box-shadow: 0 4px 18px rgba(90, 70, 30, 0.18);
  }
  .label-shapes { position: absolute; inset: 0; }
  .brand-name {
    position: absolute; left: 0; right: 0; top: 58px;
    text-align: center;
    font-weight: 700; font-size: 58px;
    color: var(--brand-green);
    letter-spacing: 1px;
  }
  .product-title {
    position: absolute; left: 88px; top: 258px;
    font-weight: 700; font-size: 98px; line-height: 84px;
    color: var(--brand-green);
    letter-spacing: 1px;
  }
  .product-type {
    position: absolute; left: 125px; top: 426px;
    width: 360px; height: 48px;
    background: var(--brand-green);
    color: #fff;
    font-weight: 700; font-size: 40px; line-height: 48px;
    letter-spacing: 14px; text-align: center;
    padding-left: 14px;
  }
  .formula-name {
    position: absolute; left: 26px; top: 490px;
    font-size: 29px; line-height: 31px;
    color: var(--ink); text-transform: uppercase;
  }
  .benefits {
    position: absolute; left: 26px; top: 588px;
    list-style: none;
    font-size: 17.5px; line-height: 23px;
    color: var(--ink);
  }
  .key-ingredient {
    position: absolute; left: 26px; top: 674px;
    font-size: 38px; color: var(--ink);
  }
  .cocoa-art {
    position: absolute; left: 248px; top: 672px;
    width: 318px; height: 160px;
    border-radius: 50%;
    background: linear-gradient(115deg, var(--leaf) 0%, var(--cocoa-mid) 50%, var(--cocoa-dark) 100%);
  }
  .claims {
    position: absolute; left: 29px; top: 900px;
    font-size: 25px; line-height: 34px;
    color: var(--ink);
  }
  .net-contents {
    position: absolute; right: 12px; bottom: 16px;
    font-size: 16px; color: var(--ink);
  }
</style>
</head>
<body>
  <div class="label">
    <svg class="label-shapes" viewBox="0 0 590 1030" width="590" height="1030" aria-hidden="true">
      <defs>
        <linearGradient id="lime-fill" x1="0" y1="0" x2="1" y2="1">
          <stop offset="0" stop-color="#b9dc45"/>
          <stop offset="1" stop-color="#a4cf23"/>
        </linearGradient>
      </defs>
      <path class="lime-field" d="M0,170 C170,140 420,100 590,34 L590,870 C430,872 220,848 0,808 Z" fill="url(#lime-fill)"/>
      <path class="swoosh-edge" d="M590,440 C430,470 310,570 318,700 C328,800 450,850 590,850 Z" fill="#f6f2b8"/>
      <path class="swoosh-panel" d="M590,462 C450,494 342,580 346,700 C352,790 462,832 590,832 Z" fill="#f1ecd3"/>
    </svg>

    <div class="brand-name">Maple Glow</div>

    <h1 class="product-title">COCOA<br>BUTTER</h1>
    <div class="product-type">LOTION</div>

    <p class="formula-name">Original<br>Moisturizing<br>Formula</p>
    <ul class="benefits">
      <li>Smoothes Dry Skin</li>
      <li>Blemishes &amp; Stretch Marks</li>
      <li>Softens Hands, Face and Body</li>
    </ul>
    <p class="key-ingredient">Vitamin E</p>

    <div class="cocoa-art" role="img" aria-label="Photo of cocoa pods, an opened pod with beans and green leaves"></div>

    <p class="claims">Smoothes Marks<br>Protect Skin</p>
    <p class="net-contents">8.5oz (250 ml)</p>
  </div>
</body>
</html>
```